Holiday Sale 2026 Graphics for New Year

I want to create 10 social media graphics (new Instagram size 4:5 (1080 x 1350 pixels) focusing on our Holiday Sale Graphics, using any of the pics attached. Use the attached pics, NO RANDOM STOCK PHOTOGRAPHY. For the color scheme of the graphics, they should all be complementary to the product colors in the photos.
You can add any of the photos attached but none are required. You can do some of the graphics in all text. I mainly need BOLD text that says one of the headlines with the pics (10 total):
1. 25% OFF Holiday Sale: New You Starts Now!
2. 25% OFF Everything: New Year, New You
3. 25% OFF Christmas Sale 🎁 Feel Amazing Again!
4. Holiday Treat: 25% OFF Your Favorites
5. 25% OFF All Supplements ✨ New Year Reset!
6. Holiday Magic: 25% OFF Every Supplement
7. 25% OFF to Kickstart Your New Year Goals
8. New Year, New Waistline! 25% OFF Sale
9. Holiday Sale: 25% OFF Everything
10. A Better You Begins With 25% OFF

```html
<!DOCTYPE html>
<html lang="en">
<head>
<meta charset="utf-8">
<title>Holiday Sale 2026 – Social Graphics</title>
<link rel="stylesheet" href="https://fonts.googleapis.com/css2?family=Anton&family=Montserrat:ital,wght@0,700;0,800;1,800;1,900&family=Yellowtail&display=swap">
<style>
  :root {
    --board: #636363;
    --card-red: #dc3831;
    --card-edge: #8a8a8a;
    --white: #ffffff;
    --yellow: #fbf24c;
    --sans: "Montserrat", Arial, sans-serif;
    --condensed: "Anton", "Impact", sans-serif;
    --script: "Yellowtail", cursive;
  }
  * { margin: 0; padding: 0; box-sizing: border-box; }
  html, body { width: 1200px; height: 1169px; overflow: hidden; background: var(--board); }
  .board { position: relative; width: 1200px; height: 1169px; }

  .post {
    position: absolute; width: 270px; height: 355px;
    background: var(--card-red);
    border: 2px solid var(--card-edge);
    box-shadow: 0 1px 3px rgba(0,0,0,.35);
    color: var(--white);
    overflow: hidden;
  }
  .col-1 { left: 44px; } .col-2 { left: 329px; } .col-3 { left: 615px; } .col-4 { left: 901px; }
  .row-1 { top: 31px; } .row-2 { top: 400px; } .row-3 { top: 769px; }

  .line { position: absolute; left: 0; right: 0; text-align: center; white-space: nowrap; }

  .kicker { font-family: var(--sans); font-weight: 700; font-size: 21px; color: var(--yellow); }
  .mega { font-family: var(--sans); font-weight: 800; font-size: 64px; line-height: 54px; letter-spacing: 1px; }
  .tag-right { font-family: var(--sans); font-weight: 700; font-size: 20px; color: var(--yellow); text-align: right; }
  .script { font-family: var(--script); font-size: 21px; }
  .script-lg { font-family: var(--script); font-size: 25px; }
  .headline { font-family: var(--condensed); font-size: 70px; line-height: 68px; text-transform: uppercase; }
  .headline-sm { font-family: var(--condensed); font-size: 56px; line-height: 52px; }
  .fine { font-family: var(--sans); font-weight: 700; font-size: 13.5px; color: var(--yellow); }
  .punch { font-family: var(--sans); font-weight: 900; font-style: italic; color: var(--yellow); }

  .pct { display: flex; justify-content: center; align-items: flex-start; font-family: var(--sans); font-weight: 700; }
  .pct-num { font-size: 76px; line-height: 62px; letter-spacing: 1px; }
  .pct-side { display: flex; flex-direction: column; align-items: center; margin-left: 4px; }
  .pct-sign { font-size: 40px; line-height: 34px; }
  .pct-off { font-size: 18px; line-height: 22px; font-weight: 800; }
</style>
</head>
<body>
<main class="board">

  <!-- 1 -->
  <section class="post col-1 row-1">
    <p class="line kicker" style="top:44px; left:45px; text-align:left;">HOLIDAY</p>
    <p class="line mega" style="top:72px; left:40px; text-align:left;">SALE<br>SALE<br>SALE</p>
    <p class="line tag-right" style="top:240px; right:48px;">25% OFF</p>
    <p class="line script" style="top:272px;">New You Starts Now!</p>
  </section>

  <!-- 2 -->
  <section class="post col-2 row-1">
    <div class="line pct" style="top:112px;"><span class="pct-num">25</span><span class="pct-side"><span class="pct-sign">%</span><span class="pct-off">OFF</span></span></div>
    <p class="line punch" style="top:180px; font-size:26px;">EVERYTHING</p>
    <p class="line script" style="top:220px;">New Year, New You!</p>
  </section>

  <!-- 3 -->
  <section class="post col-3 row-1">
    <p class="line kicker" style="top:100px; left:42px; text-align:left;">CHRISTMAS</p>
    <p class="line mega" style="top:128px; left:40px; text-align:left; font-size:66px;">SALE</p>
    <p class="line tag-right" style="top:190px; right:50px;">25% OFF</p>
    <p class="line script" style="top:222px;">Feel Amazing Again!</p>
  </section>

  <!-- 4 -->
  <section class="post col-4 row-1">
    <h2 class="line headline" style="top:88px;">Holiday<br>Treat</h2>
    <p class="line fine" style="top:240px;">25% OFF YOUR FAVORITES</p>
  </section>

  <!-- 5 -->
  <section class="post col-1 row-2">
    <div class="line pct" style="top:94px;"><span class="pct-num">25</span><span class="pct-side"><span class="pct-sign">%</span><span class="pct-off">OFF</span></span></div>
    <p class="line punch" style="top:168px; font-size:19px;">ALL SUPPLEMENTS</p>
    <p class="line script" style="top:204px; font-size:19px;">New Year Reset!</p>
  </section>

  <!-- 6 -->
  <section class="post col-2 row-2">
    <h2 class="line headline" style="top:86px;">Holiday<br>Magic</h2>
    <p class="line fine" style="top:242px; font-size:12.5px;">25% OFF EVERY SUPPLEMENT</p>
  </section>

  <!-- 7 -->
  <section class="post col-3 row-2">
    <div class="line pct" style="top:94px;"><span class="pct-num">25</span><span class="pct-side"><span class="pct-sign">%</span><span class="pct-off">OFF</span></span></div>
    <p class="line punch" style="top:168px; font-size:19px; line-height:24px;">TO KICKSTART YOUR<br>NEW YEAR GOALS</p>
  </section>

  <!-- 8 -->
  <section class="post col-4 row-2">
    <p class="line script-lg" style="top:56px; left:34px; text-align:left;">New Year,</p>
    <p class="line script-lg" style="top:92px; left:76px; text-align:left;">New Waistline!</p>
    <div class="line pct" style="top:144px;"><span class="pct-num">25</span><span class="pct-side"><span class="pct-sign">%</span><span class="pct-off">OFF</span></span></div>
    <p class="line punch" style="top:208px; font-size:64px; line-height:64px;">SALE</p>
  </section>

  <!-- 9 -->
  <section class="post col-1 row-3">
    <h2 class="line headline" style="top:86px;">Holiday<br>Sale</h2>
    <p class="line punch" style="top:240px; font-size:15px;">25% OFF EVERYTHING!</p>
  </section>

  <!-- 10 -->
  <section class="post col-2 row-3">
    <h2 class="line headline-sm" style="top:58px;">A BETTER<br>TO BEGIN<br>WITH</h2>
    <p class="line punch" style="top:228px; font-size:38px;">25% OFF</p>
  </section>

  <!-- 11 -->
  <section class="post col-3 row-3">
    <p class="line punch" style="top:70px; left:34px; text-align:left; font-size:23px;">25% OFF</p>
    <h2 class="line headline" style="top:100px;">Holiday<br>Sale</h2>
    <p class="line script" style="top:254px;">New You Starts Now!</p>
  </section>

</main>
</body>
</html>
```